Simple web design project

We need a four page web design for a premier domestic cleaning company. We would like to see designs which use white and blue (the blue in the logo - which is attatched). Please could the tab for the pages be horizontal and at the top of the page. Our company logo is attached and should be included on each page. Ideally, we would like the foundations of each page to be the same, with the word content differing as required (word content attatched). Additionally we have attached a flyer which has been distributed to advertise our company. Please could all web designs illustrate the same professional message this flyer does.

Target Market(s)

females with higher than average income, aged 30-50. Have families and work 9-5.

Industry/Entity Type

It Company

Requirements
Must have
• logo on each page. Foundations of each page the same. phone number and email on the bottom of each page.
Should not have
• please no pictures of females cleaning.

```html
<!DOCTYPE html>
<html lang="en">
<head>
<meta charset="utf-8">
<title>Brookvale Cleaners – Premier Domestic Cleaners</title>
<link href="https://fonts.googleapis.com/css2?family=Ubuntu:wght@300;400&family=Oswald:wght@400&family=Open+Sans:ital,wght@0,400;0,600;1,400&display=swap" rel="stylesheet">
<style>
:root{
  --brand-blue:#1f5fb0;
  --sky:#0a8fd0;
  --sky-deep:#0564a8;
  --sky-light:#5fd0f5;
  --ink:#1a1a1a;
  --muted:#333;
  --footer-bg:#3a3a3a;
  --footer-text:#d6d6d6;
  --footer-link:#9a9a9a;
  --field-border:#c8c8c8;
  --tick:#7cbf2c;
}
*{margin:0;padding:0;box-sizing:border-box}
html,body{width:1200px;height:1174px;overflow:hidden;background:#fff}
body{font-family:"Open Sans",Arial,sans-serif;color:var(--ink);position:relative}

.site-header{position:absolute;left:0;top:0;width:1200px;height:125px;background:linear-gradient(#fafafa,#e9e9e9);border-bottom:1px solid #d8d8d8}
.brand{position:absolute;left:88px;top:40px}
.brand-name{font-family:"Ubuntu",sans-serif;font-size:30px;color:var(--brand-blue);display:flex;align-items:center;gap:10px}
.brand-mark{width:22px;height:22px;background:var(--brand-blue)}
.brand-tagline{font-family:"Ubuntu",sans-serif;font-size:15px;color:#222;margin:10px 0 0 54px}
.search{position:absolute;left:864px;top:22px;width:248px;height:26px;border:1px solid #d4d4d4;border-radius:13px;background:#fff;font-size:13px;padding:4px 10px;color:#222}
.search svg{position:absolute;right:8px;top:5px}
.main-nav{position:absolute;top:64px;left:584px;display:flex}
.nav-item{position:relative;width:148px}
.nav-item:last-child{width:96px}
.nav-label{display:inline-block;font-family:"Oswald",sans-serif;font-size:16px;color:#222;padding:4px 9px;border-radius:10px;text-transform:uppercase;margin-left:-9px}
.nav-label small{font-size:12px;color:#666;margin-right:3px}
.nav-item.current .nav-label{background:var(--brand-blue);color:#fff;margin-left:0}
.nav-item.current .nav-label small{color:#fff}
.nav-sub{display:block;font-style:italic;font-size:13px;color:#222;margin-top:2px}
.nav-item.current .nav-sub{margin-left:8px}

.hero{position:absolute;left:0;top:125px;width:1200px;height:367px;background:radial-gradient(ellipse at 35% 40%,#10b0e0 0%,var(--sky) 35%,var(--sky-deep) 100%)}
.hero svg{position:absolute;left:0;top:0}
.hero-copy{position:absolute;left:88px;top:120px;color:#fff;font-family:"Ubuntu",sans-serif;font-weight:300}
.hero-copy .l1{font-size:25px}
.hero-copy .l1 b{font-weight:300;font-size:38px}
.hero-copy .l2{font-size:25px;margin-top:-6px}
.hero-copy .l3{font-size:25px;margin-top:18px}
.hero-copy .l3 em{color:var(--sky-light)}

.content{position:absolute;left:88px;top:514px;width:730px}
.content h1,.content h2{font-family:"Ubuntu",sans-serif;font-weight:300;color:var(--ink)}
.content h1{font-size:31px}
.content h2{font-size:24px;margin-top:22px}
.content p{font-size:12.5px;line-height:25px;color:var(--ink)}
.intro{margin-top:12px}
.reasons{list-style:none;margin-top:14px}
.reasons li{font-size:12.5px;height:25px;display:flex;align-items:center;gap:9px}
.closing{margin-top:24px}

.quick-form{position:absolute;left:838px;top:518px;width:275px;height:363px;border:1px solid #d2d2d2;border-radius:10px;background:linear-gradient(#fff,#ebebeb);padding:18px 22px}
.quick-form h2{font-family:"Ubuntu",sans-serif;font-weight:300;font-size:24px;margin-bottom:18px}
.field{width:228px;height:28px;border:1px solid var(--field-border);background:linear-gradient(#fff,#ececec);font-size:12.5px;padding:5px 9px;margin-bottom:22px}
.field.message{height:81px;margin-bottom:16px}
.submit{display:inline-block;width:97px;height:28px;border-radius:10px;background:linear-gradient(#55a9ec,#1a6fc4);color:#fff;font-family:"Oswald",sans-serif;font-size:14px;text-align:center;line-height:28px}

.site-footer{position:absolute;left:0;top:908px;width:1200px;height:266px;background:var(--footer-bg)}
.link-col{position:absolute;top:28px}
.link-col h3{font-family:"Ubuntu",sans-serif;font-weight:400;font-size:14px;color:var(--footer-text);margin-bottom:16px}
.link-col li{list-style:none;font-size:12px;color:var(--footer-link);height:24.2px}
.search-graphic{position:absolute;left:710px;top:60px;width:108px;height:108px;border-radius:50%;background:radial-gradient(circle at 40% 40%,#5ac15a,#1c5fae 75%)}
.footer-brand{position:absolute;left:842px;top:50px;font-family:"Ubuntu",sans-serif;color:#8d8d8d}
.footer-brand .name{font-size:29px;display:flex;align-items:center;gap:10px}
.footer-brand .name span.sq{width:22px;height:22px;background:#8d8d8d}
.footer-brand .tag{font-size:15px;margin:10px 0 0 54px}
.contact{position:absolute;left:844px;color:#fff;display:flex;align-items:center;gap:12px}
.contact.phone{top:132px;font-family:"Ubuntu",sans-serif;font-size:23px}
.contact.email{top:167px;font-size:13.5px}
.copyright{position:absolute;left:844px;top:209px;color:#e5e5e5;font-size:12px;display:flex;align-items:center;gap:8px}
</style>
</head>
<body>

<header class="site-header">
  <div class="brand">
    <div class="brand-name"><span class="brand-mark"></span>Brookvale Cleaners</div>
    <div class="brand-tagline">Premier Domestic Cleaners</div>
  </div>
  <div class="search">Search
    <svg width="14" height="14" viewBox="0 0 14 14"><circle cx="8" cy="6" r="4" fill="none" stroke="#1f5fb0" stroke-width="1.6"/><line x1="5" y1="9" x2="1.5" y2="12.5" stroke="#1f5fb0" stroke-width="2"/></svg>
  </div>
  <nav class="main-nav">
    <div class="nav-item current"><span class="nav-label"><small>01</small>Home</span><span class="nav-sub">Welcome page</span></div>
    <div class="nav-item"><span class="nav-label"><small>02</small>Services</span><span class="nav-sub">What We Do</span></div>
    <div class="nav-item"><span class="nav-label"><small>03</small>Prices</span><span class="nav-sub">What We Offer</span></div>
    <div class="nav-item"><span class="nav-label"><small>04</small>Contact Us</span><span class="nav-sub">Stay in Touch</span></div>
  </nav>
</header>

<section class="hero">
  <svg width="1200" height="367" viewBox="0 0 1200 367">
    <defs>
      <linearGradient id="roomTone" x1="0" y1="0" x2="1" y2="1">
        <stop offset="0" stop-color="#d9d9d9"/>
        <stop offset="0.5" stop-color="#9a9a9a"/>
        <stop offset="1" stop-color="#4a4a4a"/>
      </linearGradient>
    </defs>
    <path role="img" aria-label="Photo of a tidy living room with a bucket of cleaning products"
      d="M556 0 H1112 V300 C1030 330 900 350 720 358 C620 362 530 340 500 300 C470 240 480 120 556 0 Z"
      fill="url(#roomTone)"/>
    <path d="M480 367 C640 350 900 350 1112 300 V318 C920 358 700 367 560 367 Z" fill="#3aa6e6" opacity="0.8"/>
  </svg>
  <div class="hero-copy">
    <div class="l1">We are a <b>premier domestic</b></div>
    <div class="l2">cleaning company based</div>
    <div class="l3">in <em>Melksham, Wiltshire.</em></div>
  </div>
</section>

<main class="content">
  <h1>Welcome to our website</h1>
  <p class="intro">We are a premier domestic cleaning company based in Melksham, Wiltshire. Our vision is to supply households with a quality, tailored cleaning service, freeing up individuals spare time and replacing the stereotypical unreliable, inconsistent cleaners.</p>
  <h2>Why Us</h2>
  <ul class="reasons">
    <li><svg width="13" height="11" viewBox="0 0 13 11"><path d="M1 6 L5 10 L12 1" fill="none" stroke="var(--tick)" stroke-width="2.4"/></svg>No contracts</li>
    <li><svg width="13" height="11" viewBox="0 0 13 11"><path d="M1 6 L5 10 L12 1" fill="none" stroke="var(--tick)" stroke-width="2.4"/></svg>Insured</li>
    <li><svg width="13" height="11" viewBox="0 0 13 11"><path d="M1 6 L5 10 L12 1" fill="none" stroke="var(--tick)" stroke-width="2.4"/></svg>Free Quotes</li>
    <li><svg width="13" height="11" viewBox="0 0 13 11"><path d="M1 6 L5 10 L12 1" fill="none" stroke="var(--tick)" stroke-width="2.4"/></svg>Personalised Service</li>
    <li><svg width="13" height="11" viewBox="0 0 13 11"><path d="M1 6 L5 10 L12 1" fill="none" stroke="var(--tick)" stroke-width="2.4"/></svg>We supply all equipment at no extra cost</li>
    <li><svg width="13" height="11" viewBox="0 0 13 11"><path d="M1 6 L5 10 L12 1" fill="none" stroke="var(--tick)" stroke-width="2.4"/></svg>Hassel free service</li>
  </ul>
  <p class="closing">Have a look through our website to see how we can help you.</p>
</main>

<aside class="quick-form">
  <h2>Quick Contact Form</h2>
  <div class="field">Name</div>
  <div class="field">Email</div>
  <div class="field">Phone</div>
  <div class="field message">Message</div>
  <span class="submit">SUBMIT</span>
</aside>

<footer class="site-footer">
  <div class="link-col" style="left:88px"><h3>Office cleaning</h3><ul><li>Links 1</li><li>Links 2</li><li>Links 3</li><li>Links 4</li><li>Links 5</li><li>Links 6</li><li>Links 7</li></ul></div>
  <div class="link-col" style="left:209px"><h3>Apartment cleaning</h3><ul><li>Links 1</li><li>Links 2</li><li>Links 3</li><li>Links 4</li><li>Links 5</li><li>Links 6</li><li>Links 7</li></ul></div>
  <div class="link-col" style="left:371px"><h3>Business Place cleaning</h3><ul><li>Links 1</li><li>Links 2</li><li>Links 3</li><li>Links 4</li><li>Links 5</li><li>Links 6</li><li>Links 7</li></ul></div>
  <div class="link-col" style="left:550px"><h3>Shopping Mall Cleaning</h3><ul><li>Links 1</li><li>Links 2</li><li>Links 3</li><li>Links 4</li><li>Links 5</li><li>Links 6</li><li>Links 7</li></ul></div>
  <div class="search-graphic" role="img" aria-label="Illustration of a globe with a magnifying glass"></div>
  <div class="footer-brand">
    <div class="name"><span class="sq"></span>Brookvale Cleaners</div>
    <div class="tag">Premier Domestic Cleaners</div>
  </div>
  <div class="contact phone">
    <svg width="22" height="22" viewBox="0 0 22 22"><rect x="0.5" y="0.5" width="21" height="21" rx="3" fill="#eee"/><path d="M7 4 C5 6 5 11 8 14 C11 17 15 18 17 16 L15 13 L13 14 C11 13 9 11 8 9 L9 7 Z" fill="#555"/></svg>
    07700 900418
  </div>
  <div class="contact email">
    <svg width="20" height="14" viewBox="0 0 20 14"><rect x="0.8" y="0.8" width="18.4" height="12.4" fill="none" stroke="#ddd" stroke-width="1.4"/><path d="M1 1 L10 8 L19 1" fill="none" stroke="#ddd" stroke-width="1.4"/></svg>
    hello@brookvalecleaners.co.uk
  </div>
  <div class="copyright">
    <svg width="13" height="13" viewBox="0 0 13 13"><circle cx="6.5" cy="6.5" r="5.6" fill="none" stroke="#e5e5e5" stroke-width="1.2"/><path d="M8.5 4.6 A2.6 2.6 0 1 0 8.5 8.4" fill="none" stroke="#e5e5e5" stroke-width="1.2"/></svg>
    2012. All Rights Reserved.
  </div>
</footer>

</body>
</html>
```